New Business Card Design Project

New business card design required for an electrical business in Australia. Offering quality electrical services including design and installation. Electrical services offered are domestic, commercial and industrial. Also meets all the air conditioning installation and maintenance needs.

Target Market(s)

The business is sleek, professional and caters primarily to wealthy clients and government contracts looking for exceptional, tailored service.

Industry/Entity Type

Electrical

Contact Information for Business Card

Damian Corlowe (Director)
0438 615 274
admin@vrtelectrical.com.au
www.vrtelectrical.com.au

Font styles to use
Sans Serif

Requirements
Must have
• The business card must show the license number - 64193 to comply with legislation.
Nice to have
• The logo colours and fonts could be incorporated into the design if the designer sees fit. We are open to new ideas and welcome creativity. The logo style guide is attached for reference if required.

```html
<!DOCTYPE html>
<html lang="en">
<head>
<meta charset="UTF-8">
<title>VRT Electrical – Business Card</title>
<link rel="stylesheet" href="https://fonts.googleapis.com/css2?family=Arimo:wght@400;700&display=swap">
<style>
  :root {
    --backdrop: #1c1c1e;
    --card-white: #ffffff;
    --navy: #14305a;
    --slate: #55575b;
    --text-grey: #5b5d61;
    --rule-grey: #c9cacc;
    --silver-light: #e4e5e7;
    --silver-mid: #b9babd;
    --silver-dark: #6b6c6f;
  }
  * { box-sizing: border-box; margin: 0; padding: 0; }
  html, body {
    width: 1200px;
    height: 1015px;
    overflow: hidden;
    background: var(--backdrop);
    font-family: "Arimo", Arial, sans-serif;
  }
  .canvas {
    width: 1200px;
    height: 1015px;
    display: flex;
    flex-direction: column;
    align-items: center;
    justify-content: center;
    gap: 48px;
  }
  .card {
    position: relative;
    width: 780px;
    height: 446px;
    overflow: hidden;
    box-shadow: 0 14px 30px rgba(0,0,0,0.55);
  }

  /* Front */
  .card-front {
    background: linear-gradient(180deg, var(--silver-dark) 0%, var(--silver-mid) 30%, var(--silver-light) 48%, var(--silver-mid) 66%, var(--silver-dark) 100%);
    display: flex;
    align-items: center;
    justify-content: center;
  }
  .front-wordmark {
    font-size: 64px;
    font-weight: 400;
    letter-spacing: 6px;
    color: #4a4b4e;
  }

  /* Back */
  .card-back { background: var(--card-white); }
  .brand {
    position: absolute;
    left: 70px;
    top: 150px;
    width: 330px;
    display: flex;
    align-items: center;
    gap: 14px;
  }
  .brand-dot {
    width: 16px;
    height: 16px;
    border-radius: 50%;
    background: var(--navy);
    flex: none;
  }
  .brand-name {
    font-size: 40px;
    font-weight: 400;
    letter-spacing: 3px;
    color: var(--navy);
    white-space: nowrap;
  }
  .divider {
    position: absolute;
    left: 430px;
    top: 90px;
    width: 1px;
    height: 170px;
    background: var(--rule-grey);
  }
  .contact {
    position: absolute;
    left: 462px;
    top: 90px;
  }
  .person-name {
    font-size: 26px;
    font-weight: 700;
    color: var(--navy);
    text-transform: uppercase;
    letter-spacing: 0.5px;
  }
  .person-role {
    font-size: 18px;
    color: var(--text-grey);
    margin-top: 2px;
  }
  .contact-list {
    list-style: none;
    margin-top: 24px;
  }
  .contact-list li {
    display: flex;
    align-items: center;
    gap: 8px;
    font-size: 18px;
    color: var(--text-grey);
    line-height: 26px;
  }
  .contact-list svg { width: 16px; height: 16px; flex: none; fill: var(--navy); }
  .contact-list .emph { color: var(--navy); }

  .band-grey {
    position: absolute;
    left: 0;
    bottom: 0;
    width: 500px;
    height: 34px;
    background: var(--slate);
    clip-path: polygon(0 0, 100% 0, 97% 100%, 0 100%);
  }
  .band-navy {
    position: absolute;
    right: 0;
    bottom: 0;
    width: 292px;
    height: 92px;
    background: var(--navy);
    clip-path: polygon(3% 0, 100% 0, 100% 100%, 0 100%);
  }
  .licence {
    position: absolute;
    right: 140px;
    bottom: 58px;
    font-size: 21px;
    color: #dfe4ec;
    letter-spacing: 0.5px;
  }
</style>
</head>
<body>
<main class="canvas">
  <section class="card card-front" aria-label="Card front">
    <div class="front-wordmark">VRT ELECTRICAL</div>
  </section>

  <section class="card card-back" aria-label="Card back">
    <div class="brand">
      <span class="brand-dot"></span>
      <span class="brand-name">VRT Electrical</span>
    </div>
    <div class="divider"></div>
    <div class="contact">
      <h1 class="person-name">Damian Corlowe</h1>
      <p class="person-role">Director</p>
      <ul class="contact-list">
        <li>
          <svg viewBox="0 0 24 24" aria-hidden="true"><path d="M6.6 10.8a15.1 15.1 0 0 0 6.6 6.6l2.2-2.2a1 1 0 0 1 1-.25 11.4 11.4 0 0 0 3.6.57 1 1 0 0 1 1 1V20a1 1 0 0 1-1 1A17 17 0 0 1 3 4a1 1 0 0 1 1-1h3.5a1 1 0 0 1 1 1c0 1.25.2 2.45.57 3.57a1 1 0 0 1-.25 1z"/></svg>
          0438 615 274
        </li>
        <li>
          <svg viewBox="0 0 24 24" aria-hidden="true"><path d="M2 5h20v14H2zm2 2v.5l8 5 8-5V7l-8 5z"/></svg>
          admin@vrtelectrical.com.au
        </li>
        <li>
          <svg viewBox="0 0 24 24" aria-hidden="true"><path d="M12 2a10 10 0 1 0 0 20 10 10 0 0 0 0-20zm0 2c.9 0 2.2 1.8 2.8 5H9.2C9.8 5.8 11.1 4 12 4zM4.3 9h2.9a18 18 0 0 0 0 6H4.3a8 8 0 0 1 0-6zm4.9 6a16 16 0 0 1 0-6h5.6a16 16 0 0 1 0 6zm7.6 0a18 18 0 0 0 0-6h2.9a8 8 0 0 1 0 6zM12 20c-.9 0-2.2-1.8-2.8-5h5.6c-.6 3.2-1.9 5-2.8 5z"/></svg>
          <span>www.<span class="emph">vrtelectrical</span>.com.au</span>
        </li>
      </ul>
    </div>
    <div class="band-grey"></div>
    <div class="band-navy"></div>
    <p class="licence">LIC NO: 64193</p>
  </section>
</main>
</body>
</html>
```